Company Vehicle sign writing design

Looking for a vehicle signwriting design that looks professional and modern, we always purchase white vehicles so needs to work for this, we don't want an overly complex design but clean and sharp.

Our logo needs to be on the side and rear of the vehicle, with the company address on the rear, which is "83 Larkfield Street, Wesmoor, Christchurch www.bqx.kiwi"

Use of black sections or dashes could be used.

No other colours apart from black, white and grey are to be used.

Either inverted logos can be used.

Target Market(s)

Trucking company owners

Font styles to use
Other font styles liked:
• Helvetica Neue

Colors

Designer to choose only greyscale colors for use in the design.

Requirements
Must have
• Logo on side and rear
Nice to have
• Clean crisp design with logos not too large.
Should not have
• Any color apart from black, white and grey.
• The "BQX Haulbeds" text should always be with the emblem
• The "BQX Haulbeds" font should next change.

```html
<!DOCTYPE html>
<html lang="en">
<head>
<meta charset="utf-8">
<title>BQX Haulbeds – Vehicle Signwriting</title>
<link href="https://fonts.googleapis.com/css2?family=Roboto+Condensed:wght@700&display=swap" rel="stylesheet">
<style>
  :root {
    --ink: #0d0d0f;
    --white: #ffffff;
    --grey: #9a9a9c;
    --seam: #3a3a3c;
    --ground: #ececec;
    --type: "Roboto Condensed", "Helvetica Neue", Arial, sans-serif;
  }
  * { box-sizing: border-box; margin: 0; padding: 0; }
  html, body { width: 1200px; height: 1200px; overflow: hidden; }
  body { background: var(--ground); position: relative; font-family: var(--type); font-weight: 700; color: var(--white); }

  .panel { position: absolute; background: var(--ink); overflow: hidden; }
  .accent { position: absolute; left: 0; bottom: 0; }
  .accent polygon { fill: var(--grey); }

  .brand { position: absolute; display: flex; align-items: center; gap: 14px; }
  .brand__mark { background: var(--white); flex: none; }
  .brand__name { line-height: 0.95; text-transform: uppercase; letter-spacing: 0.01em; }

  .address { position: absolute; font-size: 15px; line-height: 1.45; }

  /* Rear doors */
  .rear { left: 330px; top: 50px; width: 540px; height: 520px; }
  .rear__seam { position: absolute; top: 0; bottom: 0; width: 8px; background: var(--seam); }
  .rear__seam--a { left: 266px; }
  .rear__seam--b { left: 286px; }
  .rear .brand--door-left { left: 40px; top: 150px; }
  .rear .brand--door-left .brand__mark { width: 34px; height: 34px; }
  .rear .brand--door-left .brand__name { font-size: 34px; }
  .rear .address { left: 40px; top: 270px; }
  .rear .brand--door-right { left: 318px; top: 160px; }
  .rear .brand--door-right .brand__name { font-size: 34px; }

  /* Cab door */
  .cab { left: 40px; top: 700px; width: 320px; height: 210px; }
  .cab .address { left: 120px; top: 62px; font-size: 17px; }

  /* Trailer side */
  .side { left: 400px; top: 620px; width: 760px; height: 480px; }
  .side .brand { right: 80px; top: 120px; }
  .side .brand__mark { width: 40px; height: 40px; }
  .side .brand__name { font-size: 40px; }
</style>
</head>
<body>

  <section class="panel rear" aria-label="Rear doors">
    <div class="rear__seam rear__seam--a"></div>
    <div class="rear__seam rear__seam--b"></div>
    <svg class="accent" width="200" height="200" viewBox="0 0 200 200" aria-hidden="true">
      <polygon points="0,0 0,200 190,200"/>
    </svg>
    <div class="brand brand--door-left">
      <span class="brand__mark"></span>
      <span class="brand__name">BQX<br>Haulbeds</span>
    </div>
    <p class="address">83 Larkfield Street<br>Wesmoor, Christchurch<br>www.bqx.kiwi</p>
    <div class="brand brand--door-right">
      <span class="brand__name">BQX<br>Haulbeds</span>
    </div>
  </section>

  <section class="panel cab" aria-label="Cab door">
    <svg class="accent" width="320" height="210" viewBox="0 0 320 210" aria-hidden="true">
      <polygon points="0,0 0,210 140,210"/>
    </svg>
    <p class="address">83 Larkfield Street<br>Wesmoor, Christchurch<br>www.bqx.kiwi</p>
  </section>

  <section class="panel side" aria-label="Trailer side">
    <svg class="accent" width="760" height="480" viewBox="0 0 760 480" aria-hidden="true">
      <polygon points="30,150 30,440 300,440"/>
    </svg>
    <div class="brand">
      <span class="brand__mark"></span>
      <span class="brand__name">BQX<br>Haulbeds</span>
    </div>
  </section>

</body>
</html>
```